Travel video blogger needs website design

I need a website designed for my new travel video blog "Roaming Sparrow". I have only just started but need a website that is fairly simple and not too busy. I have a logo which I want on it (I have attached it to this project). I also want a link to all my other social medias on the main page (vidtrekhub, Snapwell and Palnook) and my videos as well. Here is a link to my vidtrekhub page for you to look at: https://www.vidtrekhub.net/channel/QRm4tZ8pWnE2HX57YKccd31v
As I have only just started and I am still trying to find my specific niche, again I need it to be sleek and simple that I can go in and change slightly here and there. I would like these pages on the website: About Me, Videos, Social Media, Blog, Gallery, contact me. for an example I like the look of www.theroamingkinfolk.net website.

I already have the domain and I am with Harborweb with pagecraftr.org. I just want to spend my time getting better and learning about videos then trying to create a website (I am a bit of a perfectionist when I try to do something).

Target Market(s)

Young Adults (majority females) between the ages of 18 and 30 with an interest in travelling.

Industry/Entity Type

Travel Industry

Number of Pages Required

1 page

Colors

Designer to choose colors to be used in the design.

Requirements
Must have
• A like to my Snapwell, Palnook and vidtrekhub channels on the home page
• Must be a nice, simple design
• Must have my logo on the front and name "Roaming Sparrow"
Nice to have
• A nice light, bright coloured theme
Should not have
• A dark coloured theme

```html
<!DOCTYPE html>
<html lang="en">
<head>
<meta charset="utf-8">
<title>Roaming Sparrow — Travel Video Blog</title>
<link href="https://fonts.googleapis.com/css2?family=Questrial&family=Kalam:wght@700&display=swap" rel="stylesheet">
<style>
  :root{
    --gold:#d9b27a;
    --gold-dark:#c99c5c;
    --ink:#1b1b1b;
    --muted:#6f6f6f;
    --panel:#f4f4f4;
    --white:#ffffff;
    --footer:#000000;
    --footer-line:#3a3a3a;
  }
  *{box-sizing:border-box;margin:0;padding:0}
  html,body{width:1200px;height:2628px;overflow:hidden}
  body{position:relative;background:var(--white);font-family:"Questrial",sans-serif;color:var(--ink)}
  .abs{position:absolute}
  a{color:inherit;text-decoration:none}

  /* Header */
  .site-header{left:0;top:0;width:1200px;height:137px;background:var(--white)}
  .social-label{left:152px;top:46px;font-size:12px;color:var(--gold);letter-spacing:.5px}
  .social-links{left:232px;top:45px;font-size:12px;color:var(--muted);display:flex;gap:10px}
  .social-links a.active{color:var(--gold)}
  .call{right:150px;top:43px;font-size:15px;color:var(--ink);display:flex;align-items:center;gap:6px}
  .call .label{color:var(--gold)}
  .brand{left:450px;top:20px;width:300px;text-align:center}
  .brand-mark{display:block;margin:0 auto}
  .brand-name{display:block;font-size:13px;letter-spacing:1.5px;color:var(--ink);margin-top:10px}
  .main-nav{left:0;top:99px;width:1200px;font-size:13px;letter-spacing:.6px;color:var(--ink)}
  .main-nav a{position:absolute;top:0;transform:translateX(-50%);white-space:nowrap}
  .main-nav a.current{color:var(--gold)}
  .nav-underline{left:77px;top:122px;width:119px;height:2px;background:var(--gold)}

  /* Hero */
  .hero{left:0;top:137px;width:1200px;height:434px;background:linear-gradient(160deg,#3f5664 0%,#4e6673 40%,#6b7d84 70%,#8d8f8c 100%)}
  .hero-kicker{left:152px;top:237px;font-size:12px;color:#e8e8e8;letter-spacing:.5px}
  .hero-title{left:152px;top:264px;width:420px;font-size:29px;line-height:37px;color:var(--white);font-weight:400;letter-spacing:.5px}
  .hero-text{left:152px;top:354px;width:420px;font-size:12px;line-height:18px;color:#eaeaea}
  .btn{display:flex;align-items:center;justify-content:center;font-size:12px;letter-spacing:.5px}
  .btn-solid{background:var(--gold);color:var(--white)}
  .btn-outline{border:1px solid var(--gold);color:var(--gold)}
  .hero-btn{left:152px;top:434px;width:130px;height:34px}
  .hero-arrow{width:32px;height:32px;border-radius:50%;display:flex;align-items:center;justify-content:center}
  .hero-arrow.prev{left:1012px;top:317px;background:rgba(255,255,255,.25);border:1px solid rgba(255,255,255,.6)}
  .hero-arrow.next{left:1012px;top:357px;background:var(--white)}
  .hero-dots{left:570px;top:518px;display:flex;gap:10px}
  .hero-dots span{width:11px;height:11px;border-radius:50%;border:1.5px solid var(--white)}
  .hero-dots span.on{background:rgba(255,255,255,.6)}

  /* Section titles */
  .section-title{width:1200px;left:0;text-align:center;font-size:28px;letter-spacing:.5px;color:var(--ink)}
  .title-line{height:1.5px;background:var(--gold)}

  /* Videos */
  .videos{left:0;top:571px;width:1200px;height:752px;background:var(--panel)}
  .video-card{overflow:hidden;border:1px solid #d8d8d8}
  .video-label{position:absolute;left:22px;bottom:20px;font-family:"Kalam",cursive;font-size:28px;color:var(--white);letter-spacing:2px}
  .play{position:absolute;left:50%;top:50%;transform:translate(-50%,-50%)}
  .all-videos{left:534px;top:1226px;width:130px;height:34px;background:transparent}

  /* About */
  .about-text{left:250px;top:1440px;width:700px;text-align:center;font-size:12px;line-height:19px;color:var(--muted);letter-spacing:.4px}
  .about-btn{left:534px;top:1542px;width:130px;height:33px}

  /* Snapwell feed */
  .feed-title{left:152px;top:1634px;font-size:28px;letter-spacing:.5px}
  .feed-line{left:318px;top:1653px;width:76px;height:1.5px;background:var(--gold)}
  .feed-handle{left:152px;top:1677px;font-size:11px;color:var(--gold);letter-spacing:.4px}
  .feed-photo{overflow:hidden}
  .feed-photo.raised{box-shadow:0 10px 30px rgba(0,0,0,.25)}
  .follow-tile{left:878px;top:1906px;width:168px;height:168px;background:var(--gold);display:flex;align-items:center;justify-content:center}
  .follow-ring{width:144px;height:144px;border-radius:50%;border:1px solid rgba(255,255,255,.8);display:flex;flex-direction:column;align-items:center;justify-content:center;gap:8px;color:var(--white);font-size:12px}
  .follow-ring .dot{width:14px;height:14px;border:1.5px solid var(--white);border-radius:3px}

  /* Subscribe */
  .subscribe-text{left:0;top:2256px;width:1200px;text-align:center;font-size:12px;color:var(--muted);letter-spacing:.4px}
  .subscribe-form{left:382px;top:2300px;width:434px;height:41px;background:var(--white);border:1.5px solid var(--gold);display:flex;align-items:center;justify-content:space-between;padding:0 12px;z-index:2}
  .subscribe-form span{font-size:11px;color:#9a9a9a}

  /* Footer */
  .site-footer{left:0;top:2321px;width:1200px;height:307px;background:var(--footer)}
  .footer-brand{left:450px;top:2386px;width:300px;text-align:center;color:var(--white)}
  .footer-brand .brand-name{color:var(--white)}
  .footer-rule{top:2525px;height:1px;background:var(--footer-line)}
  .footer-social{left:0;top:2516px;width:1200px;display:flex;justify-content:center;gap:16px;font-size:12px;color:#bdbdbd}
  .footer-social a.active{color:var(--gold)}
  .copyright{left:0;top:2574px;width:1200px;text-align:center;font-size:12px;color:#cfcfcf;letter-spacing:.4px}
  .to-top{left:1122px;top:2510px;width:26px;height:26px;background:var(--gold);transform:rotate(45deg)}
</style>
</head>
<body>

<!-- Header -->
<header class="site-header abs">
  <span class="social-label abs">Get Social:</span>
  <nav class="social-links abs" aria-label="Social channels">
    <a href="#">Palnook</a>
    <a href="https://www.vidtrekhub.net/channel/QRm4tZ8pWnE2HX57YKccd31v" class="active">Vidtrekhub</a>
    <a href="#">Snapwell</a>
  </nav>
  <a class="brand abs" href="#">
    <svg class="brand-mark" width="56" height="56" viewBox="0 0 56 56" aria-hidden="true"><circle cx="28" cy="28" r="25" fill="none" stroke="#1b1b1b" stroke-width="2"/></svg>
    <span class="brand-name">ROAMING SPARROW</span>
  </a>
  <div class="call abs">
    <span class="label">Call Us:</span>
    <svg width="13" height="13" viewBox="0 0 24 24" aria-hidden="true"><path d="M6.6 10.8a15 15 0 006.6 6.6l2.2-2.2a1 1 0 011-.25 11.4 11.4 0 003.6.6 1 1 0 011 1V20a1 1 0 01-1 1A17 17 0 013 4a1 1 0 011-1h3.5a1 1 0 011 1 11.4 11.4 0 00.6 3.6 1 1 0 01-.25 1z" fill="#d9b27a"/></svg>
    <span>123-456-7890</span>
  </div>
  <nav class="main-nav abs" aria-label="Main">
    <a href="#" class="current" style="left:136px">About Me</a>
    <a href="#" style="left:281px">Videos</a>
    <a href="#" style="left:425px">Social Media</a>
    <a href="#" style="left:770px">Blog</a>
    <a href="#" style="left:916px">Gallery</a>
    <a href="#" style="left:1061px">Contact Me</a>
  </nav>
  <span class="nav-underline abs"></span>
</header>

<!-- Hero -->
<section class="hero abs" role="img" aria-label="Couple sitting together on a wooden pier beside a calm blue lake"></section>
<p class="hero-kicker abs">— Roaming Sparrow -</p>
<h1 class="hero-title abs">Contrary to Popular Belief, Lorem Ipsum is Site</h1>
<p class="hero-text abs">There are many variations of passages of Lorem Ipsum available, but the majority have suffered There are many lorem variations randomised words which...</p>
<a href="#" class="hero-btn btn btn-solid abs">Explore More</a>
<span class="hero-arrow prev abs"><svg width="10" height="10" viewBox="0 0 10 10"><path d="M6.5 1.5L3 5l3.5 3.5" fill="none" stroke="#fff" stroke-width="1.4"/></svg></span>
<span class="hero-arrow next abs"><svg width="10" height="10" viewBox="0 0 10 10"><path d="M3.5 1.5L7 5 3.5 8.5" fill="none" stroke="#555" stroke-width="1.4"/></svg></span>
<div class="hero-dots abs"><span></span><span class="on"></span><span></span></div>

<!-- Videos -->
<section class="videos abs"></section>
<span class="title-line abs" style="left:427px;top:646px;width:78px"></span>
<h2 class="section-title abs" style="top:628px">My Videos</h2>
<span class="title-line abs" style="left:696px;top:646px;width:78px"></span>

<a href="#" class="video-card abs" style="left:228px;top:696px;width:434px;height:240px;background:linear-gradient(180deg,#6f9fb3 0%,#8fa98c 45%,#4d6f78 100%)" role="img" aria-label="River with an old covered bridge in Italy"><span class="video-label">Italy</span></a>
<a href="#" class="video-card abs" style="left:689px;top:696px;width:280px;height:240px;background:linear-gradient(180deg,#2f7fc0 0%,#5aa3d6 45%,#2b6c9a 100%)" role="img" aria-label="Wooden jetty with lit huts over the water in Thailand"><span class="video-label">Thailand</span></a>
<a href="#" class="video-card abs" style="left:230px;top:965px;width:229px;height:228px;background:linear-gradient(180deg,#9bb0c4 0%,#7a4c3a 55%,#3d3a38 100%)" role="img" aria-label="Red brick gabled building by a canal in Germany"><span class="video-label">Germany</span></a>
<a href="#" class="video-card abs" style="left:485px;top:965px;width:230px;height:228px;background:linear-gradient(180deg,#8a8a8a 0%,#6d6a62 45%,#4b5a3b 100%)" role="img" aria-label="Castle with formal gardens in Scotland">
  <svg class="play" width="30" height="30" viewBox="0 0 30 30" aria-hidden="true"><circle cx="15" cy="15" r="15" fill="#d9b27a"/><path d="M12 9.5l9 5.5-9 5.5z" fill="#1b1b1b"/></svg>
  <span class="video-label">Scotland</span></a>
<a href="#" class="video-card abs" style="left:741px;top:965px;width:228px;height:228px;background:linear-gradient(180deg,#7fa0c4 0%,#b9c3cc 45%,#737a7e 100%)" role="img" aria-label="City skyline and waterfront fountain in Singapore"><span class="video-label">Singapore</span></a>
<a href="#" class="all-videos btn btn-outline abs">View All Video</a>

<!-- About -->
<span class="title-line abs" style="left:429px;top:1400px;width:78px"></span>
<h2 class="section-title abs" style="top:1382px">About Me</h2>
<span class="title-line abs" style="left:693px;top:1400px;width:78px"></span>
<p class="about-text abs">But I must explain to you how all this mistaken idea of denouncing pleasure and<br>praising pain was born and I will give you a complete account of the system, and expound the actual<br>teachings of the great explorer of the truth, the master-builder of human happiness.<br>No one rejects, dislikes, or avoids pleasure itself ...</p>
<a href="#" class="about-btn btn btn-solid abs">Discover More</a>

<!-- Snapwell feed -->
<h2 class="feed-title abs">Snapwell</h2>
<span class="feed-line abs"></span>
<a href="#" class="feed-handle abs">Follow@RoamingSparrow</a>
<div class="feed-photo abs" style="left:152px;top:1745px;width:170px;height:168px;background:linear-gradient(180deg,#6d7f8c 0%,#7c8a6a 50%,#8d8478 100%)" role="img" aria-label="Hiker with arms outstretched on a rocky mountain trail"></div>
<div class="feed-photo abs" style="left:347px;top:1794px;width:240px;height:240px;background:linear-gradient(160deg,#a9a39a 0%,#c4a07a 50%,#5a4d44 100%)" role="img" aria-label="Man in a camel coat on a city street"></div>
<div class="feed-photo raised abs" style="left:611px;top:1713px;width:170px;height:169px;background:linear-gradient(180deg,#3f3a33 0%,#6f6556 55%,#4a4238 100%)" role="img" aria-label="Woman sitting outdoors in a white top">
  <svg style="position:absolute;left:76px;top:76px" width="18" height="18" viewBox="0 0 18 18" aria-hidden="true"><path d="M9 2v14M2 9h14" stroke="#fff" stroke-width="1.6"/></svg>
</div>
<div class="feed-photo abs" style="left:804px;top:1640px;width:242px;height:240px;background:linear-gradient(180deg,#c27fa0 0%,#d99a86 45%,#8a6a4a 100%)" role="img" aria-label="Woman standing in tall grass at sunset with birds overhead"></div>
<div class="feed-photo raised abs" style="left:611px;top:1906px;width:242px;height:240px;background:linear-gradient(180deg,#7fb0d8 0%,#9aa690 40%,#c9c6c0 100%)" role="img" aria-label="Woman with a bicycle on a palm-lined street"></div>
<a href="#" class="follow-tile abs"><span class="follow-ring"><span class="dot"></span>Follow Us</span></a>

<!-- Subscribe -->
<span class="title-line abs" style="left:429px;top:2230px;width:78px"></span>
<h2 class="section-title abs" style="top:2212px">Subscribe</h2>
<span class="title-line abs" style="left:693px;top:2230px;width:78px"></span>
<p class="subscribe-text abs">Subscribe to my newsletter to get latest scoop right to your inbox.</p>

<!-- Footer -->
<footer class="site-footer abs"></footer>
<form class="subscribe-form abs">
  <span>Your email ...</span>
  <svg width="18" height="10" viewBox="0 0 18 10" aria-hidden="true"><path d="M0 5h16M12 1l4 4-4 4" fill="none" stroke="#d9b27a" stroke-width="1.3"/></svg>
</form>
<div class="footer-brand abs">
  <svg class="brand-mark" width="56" height="56" viewBox="0 0 56 56" aria-hidden="true"><circle cx="28" cy="28" r="25" fill="none" stroke="#fff" stroke-width="2"/></svg>
  <span class="brand-name">ROAMING SPARROW</span>
</div>
<span class="footer-rule abs" style="left:228px;width:290px"></span>
<span class="footer-rule abs" style="left:682px;width:287px"></span>
<nav class="footer-social abs" aria-label="Social channels">
  <a href="#">Palnook</a>
  <a href="https://www.vidtrekhub.net/channel/QRm4tZ8pWnE2HX57YKccd31v" class="active">Vidtrekhub</a>
  <a href="#">Snapwell</a>
</nav>
<p class="copyright abs">© 2018 RoamingSparrow. All Right Reserved.</p>
<a href="#" class="to-top abs" aria-label="Back to top"></a>

</body>
</html>
```